TRV Advisory Business Cards

Hi there,

I'd like to make a simple new business card design with the logo we already have created for our business.

I need a double sided business card with our logo on the front side and the company and person's details on the back side.

I'd like it to be on a white background and no background so I can potentially use it with either white paper or put it on different coloured paper in accordance with our business colours.

Please use the logo images I have attached and also the fonts.

So Front side:
- Logo in centre of business card (use medium logo so there is a pretty decent border around it, so don't want to fill the whole card but to make it prominent).

Back Side.
- We need 3 different business cards with the different people's name on each.

ie.

Dariel Moratkin
Business Development Manager

m +61 437 290 618
e dariel@trvadvisory.com.au
w trvadvisory.com.au

- Also I'd like to put only the cog/power button logo in the top right hand corner of the card.
(You might need to chop the current logo in half as I don't have a seperate log just for this)
- Also I'd like some lines running on the top left hand corner diagonally, anything that will add to the design or some swirling lines that add some cool effect to the card.

Also I'd like to maybe put our ABN in the bottom right hand corner of the card in a smaller font.

I'd like to also talk to the designer if possible so I can get my idea across a bit better.

Thanks!

Regards,
Dariel

```html
<!DOCTYPE html>
<html lang="en">
<head>
<meta charset="utf-8">
<title>TRV Advisory – Business Card</title>
<link rel="stylesheet" href="https://fonts.googleapis.com/css2?family=Righteous&display=swap">
<style>
  :root {
    --grad-top: #fba20a;
    --grad-bottom: #f5e90e;
    --ink-white: #ffffff;
    --brand-orange: #f9a60c;
  }
  html, body {
    margin: 0;
    padding: 0;
    width: 1200px;
    height: 741px;
    overflow: hidden;
    background: #ffffff;
  }
  .card {
    position: relative;
    width: 1200px;
    height: 741px;
    overflow: hidden;
    background: linear-gradient(to bottom, var(--grad-top) 0%, var(--grad-bottom) 100%);
    font-family: "Righteous", sans-serif;
    color: var(--ink-white);
  }
  .brand-mark {
    position: absolute;
    top: 0;
    left: 0;
    width: 1200px;
    height: 741px;
  }
  .brand-name {
    font-family: "Righteous", sans-serif;
    font-size: 44px;
    fill: var(--brand-orange);
  }
  .person {
    position: absolute;
    left: 98px;
    top: 232px;
    margin: 0;
    font-weight: 400;
  }
  .person-name {
    display: block;
    font-size: 37px;
    line-height: 48px;
    letter-spacing: 2.5px;
  }
  .person-role {
    display: block;
    font-size: 42px;
    line-height: 54px;
    letter-spacing: 1px;
  }
  .contact-list {
    position: absolute;
    left: 98px;
    top: 384px;
    margin: 0;
    padding: 0;
    list-style: none;
    font-size: 39px;
    line-height: 48.5px;
    letter-spacing: 1.5px;
  }
  .contact-item {
    display: flex;
  }
  .contact-label {
    width: 77px;
  }
  .abn {
    position: absolute;
    right: 87px;
    top: 640px;
    margin: 0;
    font-size: 32px;
    letter-spacing: 1px;
  }
</style>
</head>
<body>
  <main class="card">
    <svg class="brand-mark" viewBox="0 0 1200 741" role="img" aria-label="TRV Advisory brand mark">
      <circle cx="1113" cy="243" r="322" fill="#ffffff"/>
      <text class="brand-name" x="1010" y="258" text-anchor="middle">TRV Advisory</text>
    </svg>

    <h1 class="person">
      <span class="person-name">Dariel Moratkin</span>
      <span class="person-role">Business Development Manager</span>
    </h1>

    <ul class="contact-list">
      <li class="contact-item"><span class="contact-label">m</span><span class="contact-value">+61 437 290 618</span></li>
      <li class="contact-item"><span class="contact-label">e</span><span class="contact-value">dariel@trvadvisory.com.au</span></li>
      <li class="contact-item"><span class="contact-label">w</span><span class="contact-value">trvadvisory.com.au</span></li>
    </ul>

    <p class="abn">ABN: 5207 1893 346</p>
  </main>
</body>
</html>
```